Creating the Look and Feel of an Elite Boutique Consulting Practice: Vane Advisory

Complete a professional website on Weebly. As part of the site, we are open to a new logo -- we have just launched. We put up a starter website that shows you the content and theme we are going for. But clearly we aren't professional web designers and we need your help. Check out our start at vaneadvisory.com

Target Market(s)

Fortune 500 Clients

Industry/Entity Type

Management Consulting

Logo Text

VANE Advisory

Number of Pages Required

4 page

Requirements
Must have
• I've already set us up on Weebly. I'd like to give the selected designer the log-in credentials and have the designer create it on Weebly, so we can maintain it through that service.

```html
<!DOCTYPE html>
<html lang="en">
<head>
<meta charset="utf-8">
<title>Vane Advisory</title>
<link rel="stylesheet" href="https://fonts.googleapis.com/css2?family=Roboto+Condensed:wght@400&family=Open+Sans:wght@400;700&display=swap">
<style>
  :root {
    --teal: #1e8fb0;
    --teal-band: rgba(38, 150, 185, 0.85);
    --ink: #111111;
    --white: #ffffff;
    --nav-band: rgba(255, 255, 255, 0.85);
    --dark-band: rgba(20, 20, 22, 0.82);
    --green: #17a02a;
    --green-dark: #0f7e1f;
    --footer: #000000;
    --sky-top: #3d4a60;
    --sky-mid: #c9c3bb;
    --sun: #f4e2c2;
    --city-warm: #8a6a52;
    --city-dark: #3a3632;
    --object-core: #26323d;
    --object-mid: rgba(70, 82, 94, 0.75);
  }
  html, body {
    margin: 0;
    padding: 0;
    width: 1200px;
    height: 800px;
    overflow: hidden;
  }
  .page {
    position: relative;
    width: 1200px;
    height: 800px;
    overflow: hidden;
    font-family: "Roboto Condensed", "Arial Narrow", sans-serif;
  }
  .hero-photo {
    position: absolute;
    inset: 0 0 71px 0;
    background:
      radial-gradient(ellipse 420px 180px at 560px 330px, var(--sun) 0%, rgba(244,226,194,0.55) 45%, rgba(244,226,194,0) 100%),
      linear-gradient(180deg, var(--sky-top) 0%, #6e7282 18%, var(--sky-mid) 36%, #d9cfc2 46%, var(--city-warm) 60%, #6b5747 78%, var(--city-dark) 100%);
  }
  .nav-band {
    position: absolute;
    left: 0;
    top: 146px;
    width: 1200px;
    height: 72px;
    background: var(--nav-band);
  }
  .nav-link {
    position: absolute;
    top: 146px;
    line-height: 72px;
    font-size: 20px;
    color: var(--ink);
    text-decoration: none;
    letter-spacing: 0.2px;
  }
  .nav-link.is-active { color: var(--teal); }
  .nav-about { left: 93px; }
  .nav-approach { left: 250px; }
  .nav-team { left: 861px; }
  .nav-contact { left: 958px; }
  .brand-badge {
    position: absolute;
    left: 470px;
    top: 44px;
    width: 262px;
    height: 262px;
    border-radius: 50%;
    background: var(--white);
    box-shadow: 0 2px 8px rgba(0,0,0,0.35);
    display: flex;
    align-items: center;
    justify-content: center;
    z-index: 3;
  }
  .brand-name {
    font-size: 36px;
    color: var(--teal);
    text-align: center;
    line-height: 1.05;
  }
  .compass-photo {
    position: absolute;
    left: 760px;
    top: 236px;
    width: 340px;
    height: 472px;
    background: radial-gradient(ellipse 50% 50% at 50% 60%, var(--object-core) 0%, var(--object-mid) 55%, rgba(70,82,94,0) 100%);
    z-index: 2;
  }
  .tagline {
    position: absolute;
    left: 112px;
    margin: 0;
    color: var(--white);
    font-weight: 400;
  }
  .tagline-question {
    top: 385px;
    width: 698px;
    height: 73px;
    line-height: 73px;
    padding-left: 23px;
    box-sizing: border-box;
    background: var(--dark-band);
    border-radius: 4px 0 0 4px;
    font-size: 34px;
  }
  .tagline-promise {
    top: 479px;
    width: 625px;
    height: 72px;
    line-height: 72px;
    padding-left: 19px;
    box-sizing: border-box;
    background: var(--teal-band);
    font-size: 43px;
  }
  .cta-button {
    position: absolute;
    left: 112px;
    top: 573px;
    width: 282px;
    height: 66px;
    background: var(--green);
    border-bottom: 4px solid var(--green-dark);
    box-sizing: border-box;
    border-radius: 3px;
    color: var(--white);
    text-decoration: none;
    display: flex;
    align-items: center;
  }
  .cta-label {
    flex: 0 0 227px;
    box-sizing: border-box;
    font-size: 36px;
    padding-left: 16px;
    white-space: nowrap;
  }
  .cta-icon {
    flex: 1 1 auto;
    height: 100%;
    border-left: 1px solid rgba(255,255,255,0.35);
    display: flex;
    align-items: center;
    justify-content: center;
  }
  .site-footer {
    position: absolute;
    left: 0;
    bottom: 0;
    width: 1200px;
    height: 71px;
    background: var(--footer);
    color: var(--white);
    font-family: "Open Sans", Arial, sans-serif;
    font-size: 14px;
    text-align: center;
    line-height: 71px;
  }
  .site-footer strong { color: var(--teal); }
</style>
</head>
<body>
<div class="page">
  <div class="hero-photo" role="img" aria-label="Aerial view of a city skyline at sunrise under a cloudy sky"></div>

  <nav>
    <div class="nav-band"></div>
    <a class="nav-link nav-about is-active" href="#about">ABOUT VANE</a>
    <a class="nav-link nav-approach" href="#approach">APPROACH</a>
    <a class="nav-link nav-team" href="#team">TEAM</a>
    <a class="nav-link nav-contact" href="#contact">CONTACT</a>
  </nav>

  <div class="brand-badge">
    <div class="brand-name">VANE<br>Advisory</div>
  </div>

  <div class="compass-photo" role="img" aria-label="Photograph of a silver pocket compass"></div>

  <h2 class="tagline tagline-question">Do you need to transform your organization?</h2>
  <h1 class="tagline tagline-promise">Let's plot your path to success.</h1>

  <a class="cta-button" href="#about">
    <span class="cta-label">ABOUT VANE</span>
    <span class="cta-icon">
      <svg width="20" height="28" viewBox="0 0 20 28" aria-hidden="true">
        <path d="M4 3 L15 14 L4 25" fill="none" stroke="#ffffff" stroke-width="5"/>
      </svg>
    </span>
  </a>

  <footer class="site-footer">© <strong>VANE ADVISORY</strong> - 2015. All Rights Reserved.</footer>
</div>
</body>
</html>
```